Professional Coaching Business Letterhead/Footer

I need a letterhead and email footer for my personal coaching business, Dorian K Falstead Professional Coaching. I send several attachments to new clients (such as welcome letter, fee structure, etc) and would like these pages to have my branding on them.
I prefer the black and gold/silver color scheme, and will attach my logo to be used. I'd like the overall impression to be upmarket/regal/professional.

One of the uploaded files is my business card, to give an idea of the style/feel I like. The others are vector files containing logo to be used.

Target Market(s)

Corporate managers, successful business people. 30-60 yrs old.

Industry/Entity Type

Business

Requirements
Must have
• Logo (DKF)
Nice to have
• Shield emblem around logo, some type of watermark.
Should not have
• The first uploaded file is my business card, intended to show style and colors- not to be used itself as the letterhead.

```html
<!DOCTYPE html>
<html lang="en">
<head>
<meta charset="utf-8">
<title>Dorian K Falstead Professional Coaching – Stationery</title>
<link rel="stylesheet" href="https://fonts.googleapis.com/css2?family=Jost:wght@400;500;600&display=swap">
<style>
  :root{
    --stage:#7a7a7a;
    --paper:#ffffff;
    --gold:#bca52c;
    --ink:#111111;
    --text:#2b2b2b;
    --mark:#e8e9eb;
    --icon-dark:#4a4a4a;
    --social:#1f6fb0;
  }
  *{box-sizing:border-box;margin:0;padding:0}
  html,body{width:1200px;height:1000px;overflow:hidden}
  body{background:var(--stage);position:relative;font-family:"Jost",sans-serif;color:var(--text)}
  .sheet,.signature{position:absolute;background:var(--paper);overflow:hidden}
  .sheet{width:480px;height:677px;top:40px}
  .sheet--header{left:70px}
  .sheet--footer{left:626px}
  .top-rule{position:absolute;left:0;top:0;width:100%;height:6px;background:var(--gold)}
  .brand{position:absolute;text-align:center;color:var(--ink)}
  .brand__ring{display:block;margin:0 auto;border:3px solid var(--ink);border-radius:50%}
  .brand__name{display:block;font-weight:500;letter-spacing:.02em;white-space:nowrap}
  .sheet--header .brand{left:32px;top:20px;width:80px}
  .sheet--header .brand__ring{width:50px;height:50px}
  .sheet--header .brand__name{font-size:7.5px;margin-top:6px;margin-left:-10px;margin-right:-10px}
  .sheet--footer .brand{left:30px;top:19px;width:100px}
  .sheet--footer .brand__ring{width:64px;height:64px}
  .sheet--footer .brand__name{font-size:9.5px;margin-top:8px}
  .watermark{position:absolute;width:176px;height:176px;border:8px solid var(--mark);border-radius:50%;left:152px;top:307px}
  .contact{position:absolute;display:flex;align-items:flex-start}
  .contact__person{text-align:right;padding-right:8px}
  .contact__name{display:block;color:var(--gold);font-size:9px;font-weight:500;line-height:1}
  .contact__role{display:block;font-size:5.5px;color:var(--ink);font-weight:500}
  .contact__list{list-style:none;border-left:1px solid #9a9a9a;padding-left:6px}
  .contact__list li{display:flex;align-items:center;font-size:5.2px;line-height:8.4px;color:var(--ink);white-space:nowrap}
  .contact__icon{width:5px;height:5px;background:var(--gold);margin-right:4px;flex:none}
  .sheet--header .contact{right:42px;top:28px}
  .sheet--header .contact__person{padding-top:16px}
  .sheet--footer .contact{left:40px;top:636px}
  .sheet--footer .contact__person{padding-top:6px}
  .sheet--footer .contact__list + .contact__list{margin-left:10px}
  .sheet--footer .contact__list{padding-right:2px}
  .base-band{position:absolute;left:0;bottom:0;width:100%;height:10px;display:block}
  .signature{left:374px;top:761px;width:451px;height:136px}
  .signature .brand{left:20px;top:19px;width:84px}
  .signature .brand__ring{width:72px;height:72px}
  .signature .brand__name{font-size:10.5px;margin-top:12px;margin-left:-10px;margin-right:-10px}
  .signature__body{position:absolute;left:130px;top:21px;color:var(--text)}
  .signature__greeting{font-size:8.5px;font-weight:500}
  .signature__line{font-size:11px;line-height:16px;white-space:nowrap}
  .signature__name{color:var(--gold);font-size:12px;font-weight:500}
  .signature__sep{margin:0 6px;color:var(--ink)}
  .signature__role{font-size:9px}
  .signature__actions{display:flex;align-items:center;margin-top:8px}
  .action{display:flex;height:19px;margin-right:19px}
  .action__icon{width:20px;height:19px;background:var(--icon-dark);display:flex;align-items:center;justify-content:center}
  .action__label{background:var(--gold);color:#fff;font-size:9.5px;line-height:19px;padding-left:10px;width:58px}
  .social{display:flex;gap:16px;margin-left:10px}
  .social__tile{width:20px;height:20px;background:var(--social)}
</style>
</head>
<body>

<section class="sheet sheet--header" aria-label="Letterhead with header contact block">
  <div class="brand">
    <span class="brand__ring"></span>
    <span class="brand__name">DORIAN K FALSTEAD</span>
  </div>
  <div class="contact">
    <div class="contact__person">
      <span class="contact__name">Marcus Ellery</span>
      <span class="contact__role">Designation</span>
    </div>
    <ul class="contact__list">
      <li><span class="contact__icon"></span>08 5550 4281</li>
      <li><span class="contact__icon"></span>08 5550 1497</li>
      <li><span class="contact__icon"></span>office@dkf.org.au</li>
      <li><span class="contact__icon"></span>www.dkf.org.au</li>
      <li><span class="contact__icon"></span>42 Harbour Lane - Eastwood SA 5063</li>
    </ul>
  </div>
  <div class="watermark" aria-hidden="true"></div>
  <svg class="base-band" viewBox="0 0 480 10" preserveAspectRatio="none" aria-hidden="true">
    <path d="M0 2H285Q302 2 318 10H0Z" fill="var(--gold)"/>
    <path d="M310 4H480V10H325Q320 6 310 4Z" fill="var(--ink)"/>
  </svg>
</section>

<section class="sheet sheet--footer" aria-label="Letterhead with footer contact block">
  <div class="top-rule"></div>
  <div class="brand">
    <span class="brand__ring"></span>
    <span class="brand__name">DORIAN K FALSTEAD</span>
  </div>
  <div class="watermark" aria-hidden="true"></div>
  <div class="contact">
    <div class="contact__person">
      <span class="contact__name">Marcus Ellery</span>
      <span class="contact__role">Designation</span>
    </div>
    <ul class="contact__list">
      <li><span class="contact__icon"></span>08 5550 4281</li>
      <li><span class="contact__icon"></span>08 5550 1497</li>
      <li><span class="contact__icon"></span>office@dkf.org.au</li>
    </ul>
    <ul class="contact__list">
      <li><span class="contact__icon"></span>www.dkf.org.au</li>
      <li><span class="contact__icon"></span>42 Harbour Lane - Eastwood SA 5063</li>
    </ul>
  </div>
  <svg class="base-band" viewBox="0 0 480 10" preserveAspectRatio="none" aria-hidden="true">
    <path d="M0 2H285Q302 2 318 10H0Z" fill="var(--gold)"/>
    <path d="M310 4H480V10H325Q320 6 310 4Z" fill="var(--ink)"/>
  </svg>
</section>

<section class="signature" aria-label="Email signature">
  <div class="brand">
    <span class="brand__ring"></span>
    <span class="brand__name">DORIAN K FALSTEAD</span>
  </div>
  <div class="signature__body">
    <p class="signature__greeting">Best Regards,</p>
    <p class="signature__line"><span class="signature__name">Marcus Ellery</span><span class="signature__sep">|</span><span class="signature__role">Partner</span></p>
    <p class="signature__line">DORIAN K FALSTEAD<span class="signature__sep">|</span>2/88 Wren Road, City Name 7007</p>
    <p class="signature__line">Mob: 08 5550 4281<span class="signature__sep">|</span>FAX: 08 5550 1497</p>
    <div class="signature__actions">
      <div class="action">
        <span class="action__icon">
          <svg width="14" height="14" viewBox="0 0 14 14" aria-hidden="true"><g fill="none" stroke="#fff" stroke-width="1"><circle cx="7" cy="7" r="6"/><ellipse cx="7" cy="7" rx="2.6" ry="6"/><path d="M1 7H13M2 4H12M2 10H12"/></g></svg>
        </span>
        <span class="action__label">Website</span>
      </div>
      <div class="action">
        <span class="action__icon">
          <svg width="14" height="10" viewBox="0 0 14 10" aria-hidden="true"><g fill="none" stroke="#fff" stroke-width="1.2"><rect x="0.6" y="0.6" width="12.8" height="8.8"/><path d="M0.6 0.6L7 6L13.4 0.6"/></g></svg>
        </span>
        <span class="action__label">e-mail</span>
      </div>
      <div class="social" aria-label="Social links">
        <span class="social__tile"></span>
        <span class="social__tile"></span>
        <span class="social__tile"></span>
      </div>
    </div>
  </div>
  <svg class="base-band" viewBox="0 0 451 9" preserveAspectRatio="none" aria-hidden="true" style="height:9px">
    <path d="M0 2H270Q285 2 298 9H0Z" fill="var(--gold)"/>
    <path d="M288 1H451V6H305Q298 2 288 1Z" fill="var(--ink)"/>
  </svg>
</section>

</body>
</html>
```